Training company needs a Quick Reference Card design

We have draft skeleton of the design and most of the text. But we need a designer to take it the rest if the way.
I have designed a 2 page quick reference card - it is meant to be a 2-sided document. The first page is portrait, the back page can either be portrait or landscape, I'm not too concerned, whichever fits best.
Section called 'Maps' on front, a map is a collection of documents (like a manual), a topic is a document (like a page or section of a manual) and a block is a section of a document. The graphic is mean to illustrate the hierarchy but essentially a map is a big document with smaller documents in it.
Please use the company's logo colors to differentiate the different sections with minimal/ highlight only use of the darkest color, preferably.
Please use the icons for the corresponding Information types in the chart of the back - except please re-design the icons color scheme to match the company's logo/website colors.

Target Market(s)

Technical writers, after attending our training course, as an ongoing resource for them

Industry/Entity Type

It Company

Font styles to use
Sans Serif

Requirements
Must have
• Must adhere to look and feel of brand/ website. www.lumenrivet.com
Nice to have
• Please keep the design modern and slick looking, not too busy, easy to read

```html
<!DOCTYPE html>
<html lang="en">
<head>
<meta charset="utf-8">
<title>Lumen Rivet – Quick Reference Card</title>
<link rel="stylesheet" href="https://fonts.googleapis.com/css2?family=Open+Sans:wght@400;600;700&family=Roboto+Condensed:wght@400;700&display=swap">
<style>
:root{
  --blue:#2b2fe6;
  --blue-deep:#1a1fb8;
  --navy:#1b1f8a;
  --cyan:#12a3dc;
  --cyan-light:#2cb6e8;
  --charcoal:#3c3d44;
  --ink:#232323;
  --text:#3a3a3a;
  --cell:#ededf0;
  --page:#d6d6d8;
  --white:#ffffff;
}
*{box-sizing:border-box;margin:0;padding:0}
html,body{width:880px;height:1200px;overflow:hidden}
body{background:var(--page);font-family:"Open Sans",sans-serif;color:var(--text);position:relative}

/* ---------- front card ---------- */
.front{position:absolute;left:238px;top:67px;width:402px;height:570px;background:var(--white);overflow:hidden}
.brand{position:absolute;left:18px;top:24px;display:flex;align-items:center;gap:7px}
.brand-dot{width:26px;height:26px;border-radius:50%;background:var(--blue)}
.brand-name{font-family:"Open Sans",sans-serif;font-weight:700;font-size:15px;line-height:15px;color:var(--blue);letter-spacing:.2px}
.title-panel{position:absolute;left:196px;top:0;width:206px;height:75px}
.title-text{position:absolute;left:232px;top:12px;color:var(--white);font-family:"Roboto Condensed",sans-serif;font-weight:700}
.title-text .big{font-size:31px;line-height:31px;display:block}
.title-text .small{font-size:20px;line-height:22px;display:block;margin-top:2px}

.map-frame{position:absolute;left:0;top:75px;width:200px;height:170px;background:var(--cyan);padding:5px}
.map-area{position:relative;width:100%;height:100%;background:linear-gradient(135deg,#ebe8e2,#dcdad4 60%,#cfe3c9)}
.hier{position:absolute;font-size:6px;text-align:center}
.hier .lbl{font-weight:700;color:var(--ink);margin-bottom:2px;font-size:6.5px}
.pill{display:block;width:70px;height:11px;line-height:11px;border-radius:6px;color:var(--white);font-size:6.5px;margin:0 auto}
.pill.blue{background:var(--blue)}
.pill.grey{background:#5d5e66}

.defs{position:absolute;left:201px;top:75px;width:201px;height:168px;display:flex;flex-direction:column;gap:2px}
.def{flex:1;background:var(--charcoal);color:var(--white);font-size:6.6px;line-height:9.4px;font-weight:600;padding:0 18px 0 20px;display:flex;align-items:center}
.def:first-child{flex:1.3}

.band{position:absolute;left:0;height:30px;width:172px}
.band span{position:absolute;left:17px;top:8px;font-family:"Roboto Condensed",sans-serif;font-size:12.5px;color:var(--white);letter-spacing:.2px}

.rule{position:absolute;font-size:6.6px;line-height:9.6px;text-align:justify}
.rule h3{font-size:7px;font-weight:700;color:var(--cyan);text-transform:uppercase;line-height:10px}
.rule ul{list-style:none}
.rule li::before{content:"➤ ";color:var(--blue);font-size:6px}

.footer{position:absolute;left:0;top:539px;width:402px;height:31px}
.footer-bg{position:absolute;left:0;top:0;width:402px;height:31px}
.call{position:absolute;left:17px;top:7px;font-family:"Roboto Condensed",sans-serif;font-size:13px;line-height:17px;color:var(--white);white-space:nowrap}
.site{position:absolute;left:196px;top:7px;font-family:"Roboto Condensed",sans-serif;font-size:13px;line-height:17px;color:var(--white);letter-spacing:1px;white-space:nowrap}

/* ---------- back card ---------- */
.back{position:absolute;left:146px;top:714px;width:584px;height:412px;background:var(--white);overflow:hidden}
.back-base{position:absolute;left:0;top:296px;width:584px;height:116px;background:var(--charcoal)}
.back-stripe{position:absolute;left:0;top:0;width:584px;height:14px}
.icons{position:absolute;left:96px;top:26px;display:flex}
.icon{width:48px;height:28px;margin:0 19.5px;border-radius:24px 24px 0 0;display:flex;align-items:center;justify-content:center;padding-top:3px}
.icon.cyan{background:var(--cyan)}
.icon.navy{background:var(--navy)}
.table{position:absolute;left:13px;top:54px;width:547px;height:333px;border-radius:9px;overflow:hidden;display:grid;
  grid-template-columns:82px repeat(5,1fr);
  grid-template-rows:14px 48px 70px 88px 18px 56px 39px;background:var(--white);gap:0 1px;border:1px solid #cfcfd4}
.th{font-family:"Roboto Condensed",sans-serif;font-size:8px;color:var(--white);display:flex;align-items:center;justify-content:center}
.th.cyan{background:var(--cyan)}
.th.navy{background:var(--navy)}
.rh{background:var(--ink);color:var(--white);font-size:6.6px;font-weight:700;line-height:8.6px;padding:0 6px 0 8px;display:flex;align-items:center}
.td{background:var(--cell);font-size:6.6px;line-height:9.8px;padding:4px 5px 2px 6px;color:#333;border-top:1px solid #fff}
.td.short{display:flex;align-items:center;padding-top:0}
</style>
</head>
<body>

<section class="front" aria-label="Quick reference card, front">
  <div class="brand"><div class="brand-dot"></div><div class="brand-name">LUMEN<br>RIVET</div></div>
  <svg class="title-panel" viewBox="0 0 206 75" aria-hidden="true">
    <defs><linearGradient id="tg" x1="0" x2="1"><stop offset="0" stop-color="#2b2fe6"/><stop offset="1" stop-color="#1a1fb8"/></linearGradient></defs>
    <polygon points="26,0 206,0 206,75 0,75" fill="url(#tg)"/>
    <polygon points="18,0 26,0 0,75 -8,75" fill="#12a3dc"/>
  </svg>
  <div class="title-text"><span class="big">QUICK</span><span class="small">REFERENCE CARD</span></div>

  <div class="map-frame">
    <div class="map-area" role="img" aria-label="Street map background showing a location pin">
      <div class="hier" style="left:5px;top:96px"><div class="lbl">TOPIC</div><span class="pill blue">Primary Block</span><span class="pill grey" style="margin-top:10px">Sub-Block</span></div>
      <div class="hier" style="left:111px;top:96px"><div class="lbl">TOPIC</div><span class="pill grey">Primary Block</span><span class="pill blue" style="margin-top:10px">Sub-Block</span></div>
    </div>
  </div>

  <div class="defs">
    <p class="def">A map is a file that organizes topics into structured collections of information. Maps specify hierarchy and relationships among topics.</p>
    <p class="def">A topic is a group of related blocks with a title. Use the chunking principle to group together relevant blocks.</p>
    <p class="def">A block is a bite-sized chunk of information about one main idea that allows the writer to organize the material into logical sections.</p>
  </div>

  <svg class="band" style="top:243px" viewBox="0 0 172 30" aria-hidden="true"><polygon points="0,0 172,0 150,30 0,30" fill="#2b2fe6"/></svg>
  <div class="band" style="top:243px"><span>GENERAL WRITING RULES</span></div>

  <div class="rule" style="left:18px;top:290px;width:106px"><h3>Effective sentences</h3>One main agent, action &amp; outcome. Use active voice and simplest tense possible. No more than 7 sentences per paragraph. Use lists and tables.</div>
  <div class="rule" style="left:143px;top:290px;width:104px"><h3>Special characters</h3>Avoid special characters, spell out words instead. Remove parentheses, colons and dashes. Avoid using quotation marks and slashes.</div>
  <div class="rule" style="left:274px;top:290px;width:104px"><h3>Plain language</h3>Write in short sentences. Provide useful titles. Use clear familiar words. Avoid excess words. Be consistent.</div>
  <div class="rule" style="left:18px;top:366px;width:188px"><h3>3 questions to ask before you start writing:</h3>One main agent, action &amp; outcome. Use active voice and simplest tense possible. No more than 7 sentences per paragraph. Use lists and tables.</div>
  <div class="rule" style="left:223px;top:366px;width:170px;text-align:left"><h3>2 types of language arts:</h3><ul><li>LAFI – Language arts for information</li><li style="margin-top:3px">LAFPR – language arts for personal response</li></ul></div>

  <svg class="band" style="top:419px;height:28px" viewBox="0 0 172 28" aria-hidden="true"><polygon points="0,0 172,0 150,28 0,28" fill="#2b2fe6"/></svg>
  <div class="band" style="top:418px"><span>GENERAL WRITING RULES</span></div>

  <div class="rule" style="left:18px;top:453px;width:180px"><h3>Consistency</h3>Use similar terms and structures. Pick a term and stick with it. Use the same sequence of blocks. Use consistent styles.</div>
  <div class="rule" style="left:218px;top:453px;width:176px;text-align:left"><h3>Chunking</h3>Maximum of nine (7 +/- 2) items in a list, rows in a table, blocks in a topic, or topics in a map.</div>
  <div class="rule" style="left:18px;top:500px;width:180px"><h3>Relevance</h3>Group similar items together. Separate relevance? Separate block. Irrelevant? Delete it.</div>
  <div class="rule" style="left:218px;top:500px;width:176px;text-align:left"><h3>Titling</h3>Name everything. Name every block, every topic, every map and every table column.</div>

  <div class="footer">
    <svg class="footer-bg" viewBox="0 0 402 31" aria-hidden="true">
      <rect width="402" height="31" fill="#12a3dc"/>
      <polygon points="0,0 184,0 164,31 0,31" fill="#3c3d44"/>
      <polygon points="184,0 192,0 172,31 164,31" fill="#ffffff"/>
    </svg>
    <div class="call">CALL US: +1 (555) 014-2290</div>
    <div class="site">WWW.LUMENRIVET.COM</div>
  </div>
</section>

<section class="back" aria-label="Quick reference card, back">
  <svg class="back-stripe" viewBox="0 0 584 14" aria-hidden="true">
    <rect width="584" height="14" fill="#2b2fe6"/>
    <polygon points="0,0 242,0 236,14 0,14" fill="#12a3dc"/>
    <rect y="10" width="584" height="4" fill="#2cb6e8"/>
  </svg>
  <div class="back-base"></div>

  <div class="icons" aria-hidden="true">
    <div class="icon cyan"><svg width="18" height="18" viewBox="0 0 18 18"><circle cx="10" cy="3" r="2.2" fill="#1b1f8a"/><path d="M8 7h4l-2 9H6z" fill="#1b1f8a"/></svg></div>
    <div class="icon navy"><svg width="18" height="18" viewBox="0 0 18 18"><circle cx="9" cy="7" r="5.5" fill="#12a3dc"/><rect x="6.5" y="12" width="5" height="4" rx="1" fill="#12a3dc"/><path d="M9.6 3.5 7.5 7.5h2l-1 3" stroke="#1b1f8a" stroke-width="1.1" fill="none"/></svg></div>
    <div class="icon cyan"><svg width="18" height="18" viewBox="0 0 18 18"><path d="M5 16V8h1.6V3h1.6v5h.6V2h1.6v6h.6V3h1.6v5h.6V5h1.6v7a4 4 0 0 1-4 4z" fill="#fff" stroke="#1b1f8a" stroke-width=".8"/></svg></div>
    <div class="icon navy"><svg width="20" height="18" viewBox="0 0 20 18"><circle cx="7" cy="8" r="4.5" fill="none" stroke="#12a3dc" stroke-width="2.6" stroke-dasharray="2 1.4"/><circle cx="14.5" cy="12.5" r="3.2" fill="none" stroke="#12a3dc" stroke-width="2.2" stroke-dasharray="1.6 1.2"/></svg></div>
    <div class="icon cyan"><svg width="18" height="18" viewBox="0 0 18 18"><rect x="3.5" y="3" width="11" height="14" rx="1" fill="#fff" stroke="#1b1f8a" stroke-width="1"/><rect x="6.5" y="1.5" width="5" height="3" fill="#1b1f8a"/><path d="M6 13 11 6" stroke="#1b1f8a" stroke-width="1.6"/></svg></div>
  </div>

  <div class="table" role="table" aria-label="Information types">
    <div class="rh"></div>
    <div class="th cyan">REFERENCE</div><div class="th navy">CONCEPT</div><div class="th cyan">PRINCIPLE</div><div class="th navy">PROCESS</div><div class="th cyan">TASK</div>

    <div class="rh">Definition</div>
    <div class="td">Describes things the reader needs to know</div>
    <div class="td">Explains things the reader needs to understand</div>
    <div class="td">Advises the reader what they need to do or not do and when</div>
    <div class="td">Demonstrates to the reader how things work</div>
    <div class="td">Instructs the reader on how to do things</div>

    <div class="rh">Types of authoring models</div>
    <div class="td">Sentences/phrases<br>Lists (ol, ul)<br>Tables<br>Diagrams<br>Part-description<br>Part-function</div>
    <div class="td">Sentences/phrases<br>Lists (ol, ul)<br>Tables<br>Illustrations</div>
    <div class="td">Sentences/phrases<br>Lists (ol, ul)<br>Tables<br>Decision tree<br>Graphic</div>
    <div class="td">Sentences/phrases<br>Stage ordered list<br>When/then condition tree<br>Graphic example</div>
    <div class="td">Sentences/phrases<br>Lists If/then decision tree<br>Graphic example</div>

    <div class="rh">Titling best practices</div>
    <div class="td">Describes the item and anything that differentiates it from other items</div>
    <div class="td">Use the plural form of the noun, if one exists. Don’t add additional words such as “About”, “What is”, or “Definition”</div>
    <div class="td">Identifies the principle and expresses the gravity of the principle. Formula= gravity + principle, or principle + gravity</div>
    <div class="td">Human processes: Gerund of verb + noun “Grooming a dog”. System processes: Use “How (item) works” Ex“How engines work”</div>
    <div class="td">Starts with an imperative verb, do not use gerund. “Mow the lawn” “Boil and egg” “Register for a course”</div>

    <div class="rh" style="white-space:nowrap">Primary block title</div>
    <div class="td short">Introduction</div>
    <div class="td short">Definition</div>
    <div class="td short">Statement</div>
    <div class="td short">Summary</div>
    <div class="td short">Purpose</div>

    <div class="rh">Primary block content</div>
    <div class="td">Provide a description of the reference topic and how it would be used</div>
    <div class="td">Provide the exact meaning of the concept</div>
    <div class="td">Provide a high-level summary of the principle</div>
    <div class="td">Provide a short explanation of the purpose of the process, or the need for the process</div>
    <div class="td">Provide an explanation of why or when the reader would use the task</div>

    <div class="rh">Tips and examples</div>
    <div class="td"></div><div class="td"></div><div class="td"></div><div class="td"></div><div class="td"></div>
  </div>
</section>

</body>
</html>
```